To create a visually compelling, mission-aligned report that:
Presents research findings on pastoral succession and financial literacy in Lebanon.
Communicates funding opportunities to individual donors, churches, and Christian foundations.
Builds trust and credibility with potential partners.
Inspires support and engagement through storytelling, impact framing, and visual clarity.

The deliverable should be a polished report of approximately 10 - 14 pages. The report should have page breaks that are reflected in the PDF. The headings should be very clear and bold. We'd like to see colors of blues and greens and whites. We want the report to be slightly edgy and bold, but still professional and clear.

```html
<!DOCTYPE html>
<html lang="en">
<head>
<meta charset="utf-8">
<title>Leadership and Financial Health of Pastors in Lebanon – 2025 Findings</title>
<link href="https://fonts.googleapis.com/css2?family=Poppins:wght@400;500;600;700;800&display=swap" rel="stylesheet">
<style>
  :root {
    --backdrop: #161616;
    --paper: #ffffff;
    --navy: #02293a;
    --gold: #e1b225;
    --gold-deep: #a97f05;
    --ink: #111111;
    --body: #2b2b2b;
  }
  * { margin: 0; padding: 0; box-sizing: border-box; }
  html, body { width: 935px; height: 1200px; overflow: hidden; background: var(--backdrop); }
  body { position: relative; font-family: "Poppins", sans-serif; color: var(--body); }

  .page { position: absolute; background: var(--paper); overflow: hidden; }
  .page--cover { left: 26px; top: 34px; width: 430px; height: 557px; }
  .page--summary { left: 479px; top: 34px; width: 430px; height: 557px; }
  .page--cta { left: 26px; top: 613px; width: 431px; height: 557px; }
  .page--overview { left: 477px; top: 610px; width: 434px; height: 562px; }

  .corner-wedge { position: absolute; left: 0; top: 0; width: 178px; height: 27px; }
  .footer-bar { position: absolute; right: 0; bottom: 0; height: 5px; background: var(--navy); }

  /* Cover */
  .cover-photo {
    position: absolute; left: 0; top: 0; width: 430px; height: 400px;
    background: linear-gradient(180deg, #f1efec 0%, #f7f6f4 75%, #ffffff 100%);
  }
  .cover-artwork {
    position: absolute; left: 0; top: 0; width: 170px; height: 557px;
    background: linear-gradient(160deg, var(--navy) 0%, var(--navy) 35%, var(--gold-deep) 60%, var(--gold) 100%);
  }
  .cover-title {
    position: absolute; left: 172px; top: 220px; width: 250px;
    font-weight: 800; font-size: 21.5px; line-height: 30px; letter-spacing: 0.2px;
    color: var(--ink);
  }
  .cover-title .accent { color: var(--navy); }
  .brand-name {
    position: absolute; left: 300px; top: 482px; width: 130px; text-align: center;
    font-weight: 700; font-size: 12px; color: var(--navy);
  }
  .cover-byline { position: absolute; left: 272px; top: 510px; font-size: 11px; font-weight: 500; letter-spacing: 0.4px; color: var(--ink); }

  /* Inner pages */
  .block { position: absolute; left: 19px; right: 14px; }
  .section-title { font-weight: 800; font-size: 15.5px; letter-spacing: 0.3px; color: var(--navy); line-height: 20px; }
  .sub-title { font-weight: 700; font-size: 11.5px; color: var(--ink); line-height: 15px; }
  .body-text { font-size: 7.2px; line-height: 11px; color: var(--body); }
  .bullet { position: absolute; left: 19px; right: 12px; padding-left: 18px; font-size: 7.2px; line-height: 11px; color: var(--body); }
  .bullet::before {
    content: ""; position: absolute; left: 0; top: 2px;
    width: 8px; height: 8px; border-radius: 50%; background: var(--navy);
  }
</style>
</head>
<body>

  <section class="page page--cover">
    <div class="cover-photo" role="img" aria-label="Photo of two people walking away through thick morning fog"></div>
    <div class="cover-artwork" role="img" aria-label="Folded navy and gold geometric artwork"></div>
    <h1 class="cover-title">
      <span class="accent">LEADERSHIP AND FINANCIAL HEALTH</span> OF PASTORS IN LEBANON 2025 FINDINGS
    </h1>
    <p class="brand-name">kindlewell</p>
    <p class="cover-byline">A REPORT BY KINDLEWELL</p>
  </section>

  <section class="page page--summary">
    <svg class="corner-wedge" viewBox="0 0 178 27"><polygon points="0,0 178,0 0,26" fill="var(--gold)"/></svg>

    <h2 class="block section-title" style="top:41px">EXECUTIVE SUMMARY</h2>
    <h3 class="block sub-title" style="top:67px">Purpose, Scope &amp; Methodology</h3>
    <p class="block body-text" style="top:91px">In early 2025, Kindlewell conducted a field-based survey to assess the preparedness of Christian ministry leaders in Lebanon regarding two critical areas: (1) leadership succession and (2) financial management. The goal was to move beyond assumptions and gather tangible, data-driven insights that could inform strategic interventions and donor partnerships.</p>
    <p class="block body-text" style="top:142px">The study involved 26 face-to-face interviews with pastors and ministry leaders across Lebanon—both urban and rural—spanning Baptist, Nazarene, and Church of God traditions. The majority of respondents were lead pastors with a median age of 55 and an average of 20 years in ministry. Interviews were conducted in Arabic, translated into English, and analyzed by Kindlewell in partnership with Open Gate, a ministry based in Beirut.</p>

    <h3 class="block sub-title" style="top:213px">Key Findings: Succession Planning &amp; Ministry Continuity</h3>
    <p class="bullet" style="top:237px">While the majority (69%) of pastors interviewed report having a succession plan, less than one-third were able to share tangible information about the succession plan (e.g. who, what, when and how), raising concerns about the sustainability of churches and ministry to span across multiple generations.</p>
    <p class="bullet" style="top:282px">Many churches face a leadership pipeline problem, citing generational differences, emigration, or other macro-influences</p>
    <p class="bullet" style="top:311px">Legacy matters deeply to pastors, but a lack of structured transition planning undermines ministry continuity</p>

    <h3 class="block sub-title" style="top:351px">Key Findings: Ministry &amp; Personal Financial Management</h3>
    <p class="bullet" style="top:375px">The majority of pastors (73%) report significant financial stress, largely driven by: small church budgets (under $30,000 USD annually), facility rental costs, declining donor support, economic uncertainty</p>
    <p class="bullet" style="top:409px;right:4px">While most churches have oversight committees and balance sheets, few have long-term planning tools or paid staff.</p>
    <p class="bullet" style="top:440px">Less than one in five pastors save consistently, and retirement readiness is virtually nonexistent</p>

    <h3 class="block sub-title" style="top:475px">Key Findings: Openness to Education &amp; Training</h3>
    <p class="bullet" style="top:499px">Pastors expressed widespread interest in receiving practical training in budgeting, saving, stewardship, and long-term planning.</p>

    <div class="footer-bar" style="width:243px"></div>
  </section>

  <section class="page page--cta">
    <svg class="corner-wedge" viewBox="0 0 178 27"><polygon points="0,0 178,0 0,26" fill="var(--gold)"/></svg>

    <p class="bullet" style="top:56px;right:60px">Many see financial literacy as part of their spiritual and leadership responsibility, especially in stewarding churches through economic hardship</p>

    <h3 class="block sub-title" style="top:90px">Call to Action</h3>
    <p class="block body-text" style="top:114px;left:21px;right:28px">The findings reveal both promise and peril. While many pastors are deeply committed and aware of succession needs, financial instability and poor saving habits threaten their ability to retire and therefore delegate leadership responsibility to the next generation. As a result, churches and ministries alike face an existential threat — risk becoming obsolete at the end of a leader’s “career” as a minister. However, the data also points to a high-leverage opportunity: pastors are eager to learn, adapt, and lead—if equipped with the right tools and support.</p>
    <p class="block body-text" style="top:190px;left:21px;right:60px">Kindlewell invites partners to review the findings in this study to better understand the current situation facing faithful church leaders in the Middle East. Together, let’s partner together by investing in leadership pipelines, financial literacy initiatives, and sustainability strategies that will empower church leaders in Lebanon and beyond.</p>

    <div class="footer-bar" style="width:243px"></div>
  </section>

  <section class="page page--overview">
    <svg class="corner-wedge" viewBox="0 0 178 27"><polygon points="0,0 178,0 0,26" fill="var(--gold)"/></svg>

    <h2 class="block section-title" style="top:41px">OVERVIEW</h2>
    <p class="block body-text" style="top:68px;right:22px">In 2025, Kindlewell launched a preliminary study to understand the landscape of Christian leaders/pastors in Lebanon and other countries in the Middle East as it relates to leadership transition planning and finances. With the goal of using tangible data and insights rather than hunches and anecdotal observations, Kindlewell intends to use the insights gained from this study to inform how it can serve church and ministry leaders across the Middle East as well as advocate on their behalf to donors and partners.</p>
    <p class="block body-text" style="top:134px;right:22px">This study summarizes insights from 26 face-to-face interviews with Christian pastors and ministry leaders across Lebanon between March and June of 2025 relative to the guiding research question: How do Christian pastors in the Middle East practically prepare for the leadership transition of their ministry to the next generation while simultaneously managing personal and ministry related finances?</p>
    <p class="block body-text" style="top:190px;right:22px">The participants are overwhelmingly lead pastors (21/26), spanning Baptist, Nazarene, and Church of God traditions, and representing a roughly equal split between both rural and urban settings for their ministry. Respondents report a median age of 55 years and a median tenure in ministry of 20 years. Church ages vary widely, with approximately one third of churches 50 years or older. Most ministries are still in their first-generation, though several report multi-generational ministries, including one church currently in its 6th generation.</p>
    <p class="block body-text" style="top:267px;right:22px">Two themes dominate the study: (1) leadership succession importance, and (2) financial management under sustained economic pressure. A large majority indicate they have a succession plan and many have identified a successor, signaling the importance of the next generation of leadership, yet the narratives and tangibles around how and when to hand over are ambiguous.</p>
    <p class="block body-text" style="top:323px;right:22px">Financially, budgets tend to be modest. Typical annual budgets for churches are between $5,000 – $30,000 USD. While some type of formal oversight is common (e.g. financial committees preparing budgets), cash constraints, rent, physical space availability/cost, and congregational giving capacity are recurring stressors for ministry leaders. Personal saving and retirement readiness among leaders are effectively non-existent, thus presenting a practical dilemma at the time of succession.</p>
    <p class="block body-text" style="top:390px;right:22px">Below is a more in-depth discussion of the findings from the study, including a description of the methodology, key findings, analysis patterns, and conclusion.</p>

    <div class="footer-bar" style="width:245px"></div>
  </section>

</body>
</html>
```